Business Card for premium dental clinic

We are a premium dental clinic based in Brasov, Romania with more than 15 year on the market, providing quality dental treatment made by a team of more specialized dentists, working with modern equipment as a solution to beautiful and healthy teeth.

Our current logo for the clinic use 2 square with colors black and gold - dr Corbescu - studio, using family fonts Bodoni, Myriad Pro and Segoe Print.
Depending on the printing we used some gold CMYK background or gold foil picture background or a gold gradient.
We want a business card:
- eye catching business card
- distinguished business card
- premium design
- to keep the color scheme of black and gold
- to attract the customers to spent time reading the information
- modern concept

```html
<!DOCTYPE html>
<html lang="en">
<head>
<meta charset="utf-8">
<title>dr Corbescu studio – business card</title>
<link href="https://fonts.googleapis.com/css2?family=Bodoni+Moda:wght@400&family=Oswald:wght@400&family=PT+Sans+Narrow&family=Open+Sans&display=swap" rel="stylesheet">
<style>
  :root{
    --paper:#ece8e2;
    --black:#050505;
    --white:#ffffff;
    --soft-white:#efefee;
    --gold-dark:#b07a12;
    --gold:#d9a82c;
    --gold-light:#f5d86e;
    --gold-accent:#f6c33a;
  }
  *{margin:0;padding:0;box-sizing:border-box}
  html,body{width:1200px;height:1200px;overflow:hidden;background:var(--paper)}
  .canvas{position:relative;width:1200px;height:1200px}

  /* front side */
  .card-front{
    position:absolute;left:180px;top:90px;width:818px;height:462px;
    background:var(--white);padding:5px;display:flex;
    box-shadow:0 10px 24px rgba(0,0,0,.18);
  }
  .gold-foil{
    background:linear-gradient(135deg,var(--gold-light) 0%,var(--gold) 35%,var(--gold-dark) 60%,var(--gold-light) 85%,var(--gold) 100%);
  }
  .front-gold{position:relative;width:403px;height:100%}
  .name-plate{
    position:absolute;left:49px;top:149px;width:354px;height:156px;
    background:var(--white);display:flex;align-items:center;justify-content:center;
  }
  .name-plate span{
    font-family:"Oswald",sans-serif;font-size:66px;color:#222;letter-spacing:.5px;
  }
  .front-black{position:relative;flex:1;height:100%;background:var(--black)}
  .studio-word{
    position:absolute;left:66px;top:180px;
    font-family:"Oswald",sans-serif;font-size:66px;color:var(--white);
  }
  .tagline{
    position:absolute;right:18px;bottom:12px;
    font-family:"Oswald",sans-serif;font-size:46px;color:var(--white);
  }

  /* back side */
  .card-back{
    position:absolute;left:192px;top:626px;width:816px;height:466px;
    background:var(--black);overflow:hidden;
    box-shadow:0 10px 24px rgba(0,0,0,.18);
  }
  .back-waves{position:absolute;inset:0}
  .back-title{
    position:absolute;left:45px;top:64px;
    font-family:"Bodoni Moda",serif;font-size:50px;color:var(--white);
  }
  .contact-list{position:absolute;left:111px;top:212px;list-style:none}
  .contact-item{display:flex;align-items:center;color:var(--white);margin-bottom:24px}
  .contact-icon{
    width:36px;height:36px;border-radius:50%;background:var(--gold-accent);
    border:2px solid var(--white);display:flex;align-items:center;justify-content:center;flex:none;
  }
  .contact-text{margin-left:18px}
  .contact-phone{font-family:"Open Sans",sans-serif;font-size:24px}
  .contact-address{font-family:"PT Sans Narrow",sans-serif;font-size:19px;line-height:1.35}
  .contact-web{font-family:"Open Sans",sans-serif;font-size:22px}
  .tooth-art{
    position:absolute;left:483px;top:110px;width:333px;height:356px;
    background:linear-gradient(160deg,var(--soft-white),#dcdcda);
    border-top-left-radius:150px 120px;
    border-left:10px solid var(--gold-accent);
  }
</style>
</head>
<body>
<div class="canvas">

  <section class="card-front">
    <div class="front-gold gold-foil" role="img" aria-label="gold foil texture background">
      <div class="name-plate"><span>dr. corbescu</span></div>
    </div>
    <div class="front-black">
      <div class="studio-word">studio</div>
      <div class="tagline">dental clinic</div>
    </div>
  </section>

  <section class="card-back">
    <svg class="back-waves" width="816" height="466" viewBox="0 0 816 466" aria-hidden="true">
      <defs>
        <linearGradient id="goldSweep" x1="0" y1="0" x2="1" y2="1">
          <stop offset="0" stop-color="#f5d86e"/>
          <stop offset=".4" stop-color="#d9a82c"/>
          <stop offset=".7" stop-color="#b07a12"/>
          <stop offset="1" stop-color="#f0cc5a"/>
        </linearGradient>
      </defs>
      <path d="M0 0 H816 V190 C760 150 640 90 470 70 C300 50 120 50 0 42 Z" fill="url(#goldSweep)" role="img" aria-label="gold foil texture band"/>
    </svg>

    <div class="back-title">dr Corbescu - studio</div>

    <ul class="contact-list">
      <li class="contact-item">
        <span class="contact-icon">
          <svg width="20" height="20" viewBox="0 0 24 24"><path fill="#fff" d="M6.6 10.8a15 15 0 0 0 6.6 6.6l2.2-2.2c.3-.3.7-.4 1-.2 1.1.4 2.3.6 3.6.6.6 0 1 .4 1 1V20c0 .6-.4 1-1 1A17 17 0 0 1 3 4c0-.6.4-1 1-1h3.5c.6 0 1 .4 1 1 0 1.3.2 2.5.6 3.6.1.3 0 .7-.2 1z"/></svg>
        </span>
        <span class="contact-text contact-phone">+40 268 555 019</span>
      </li>
      <li class="contact-item">
        <span class="contact-icon">
          <svg width="18" height="20" viewBox="0 0 24 24"><path fill="#fff" d="M12 2a7 7 0 0 0-7 7c0 5.2 7 13 7 13s7-7.8 7-13a7 7 0 0 0-7-7zm0 9.5A2.5 2.5 0 1 1 12 6.5a2.5 2.5 0 0 1 0 5z"/></svg>
        </span>
        <span class="contact-text contact-address">strada Livezii nr 7 (4,212.75 km)<br>500410 Brasov, Romania</span>
      </li>
      <li class="contact-item">
        <span class="contact-icon">
          <svg width="20" height="20" viewBox="0 0 24 24" fill="none" stroke="#fff" stroke-width="2"><circle cx="12" cy="12" r="9"/><path d="M3 12h18M12 3c3 3 3 15 0 18M12 3c-3 3-3 15 0 18"/></svg>
        </span>
        <span class="contact-text contact-web">www.drcorbescu.ro</span>
      </li>
    </ul>

    <div class="tooth-art" role="img" aria-label="large white tooth illustration with gold outline"></div>
  </section>

</div>
</body>
</html>
```